Robotic Physical Therapy office needs a Grand Opening Flyer

We need a Grand Opening flyer design for a robotic physical therapy office named Kestrel Motion Therapy. We would like it to have a clean, classy, upscale feeling that gives potential clients a V.I.P. feeling. We would like to use the colors black, gray, and yellow (logo will be uploaded).

Event: Thursday, June 1st, 2023 from 12pm-6pm
location: 58240 Harlan Crest Ave, Pinegate Hollow, MI 48917

Industry/Entity Type

Physical therapy

Font styles to use
Script

Colors

Designer to choose colors to be used in the design.

Requirements
Nice to have
• More of a vip feel for the invite

```html
<!DOCTYPE html>
<html lang="en">
<head>
<meta charset="utf-8">
<title>Kestrel Motion Therapy — Grand Opening</title>
<link rel="stylesheet" href="https://fonts.googleapis.com/css2?family=Cinzel:wght@700&family=Lato:wght@300;400&display=swap">
<style>
  :root {
    --backdrop: #c7c8ca;
    --flyer-bg: #2c2b2c;
    --accent-yellow: #f2d22c;
    --text-light: #f2f2f2;
    --rule: #bdbdbd;
    --photo-light: #d9d9d9;
    --photo-mid: #7a7a7a;
    --photo-dark: #2c2b2c;
  }
  * { margin: 0; padding: 0; box-sizing: border-box; }
  html, body {
    width: 1200px; height: 1050px; overflow: hidden;
    background: var(--backdrop);
  }
  .canvas {
    width: 1200px; height: 1050px;
    display: flex; align-items: center; justify-content: center;
  }
  .flyer {
    position: relative;
    width: 760px; height: 984px;
    background: var(--flyer-bg);
    overflow: hidden;
    font-family: "Lato", sans-serif;
    color: var(--text-light);
    text-align: center;
  }
  .hero-photo {
    position: absolute; left: 0; top: 228px;
    width: 760px; height: 560px;
    background:
      radial-gradient(ellipse 420px 220px at 35% 22%, var(--photo-light) 0%, rgba(150,150,150,0.6) 45%, rgba(44,43,44,0) 100%),
      radial-gradient(ellipse 360px 300px at 70% 55%, var(--photo-mid) 0%, rgba(44,43,44,0) 100%),
      linear-gradient(180deg, rgba(44,43,44,0) 0%, rgba(44,43,44,0.2) 60%, var(--photo-dark) 100%),
      linear-gradient(90deg, #6d6d6d 0%, #8a8a8a 40%, #4a4a4a 100%);
    -webkit-mask-image: linear-gradient(180deg, transparent 0%, #000 12%, #000 70%, transparent 100%);
            mask-image: linear-gradient(180deg, transparent 0%, #000 12%, #000 70%, transparent 100%);
  }
  .headline {
    position: absolute; left: 0; right: 0; top: 56px;
    font-family: "Cinzel", serif;
    font-weight: 700;
    font-size: 68px;
    line-height: 56px;
    color: var(--accent-yellow);
    letter-spacing: 1px;
  }
  .subtitle {
    position: absolute; left: 169px; top: 179px;
    width: 422px;
    border-top: 1px solid var(--rule);
    border-bottom: 1px solid var(--rule);
    padding: 5px 0 4px;
    font-weight: 300;
    font-size: 31px;
    line-height: 34px;
    letter-spacing: 0.5px;
    white-space: nowrap;
  }
  .details { position: absolute; left: 0; right: 0; top: 658px; }
  .details-label {
    font-size: 18px; line-height: 24px;
    color: var(--accent-yellow);
    font-weight: 400;
  }
  .details-value {
    font-size: 17px; line-height: 24px;
    font-weight: 300;
    margin-bottom: 21px;
  }
  .brand {
    position: absolute; left: 0; right: 0; top: 866px;
    display: flex; align-items: center; justify-content: center; gap: 14px;
  }
  .brand-dot {
    width: 46px; height: 46px; border-radius: 50%;
    background: var(--accent-yellow);
  }
  .brand-name {
    font-size: 28px; font-weight: 400;
    color: var(--text-light);
    letter-spacing: 0.5px;
  }
</style>
</head>
<body>
<main class="canvas">
  <article class="flyer">
    <div class="hero-photo" role="img" aria-label="Black and white photo of a hand gripping the handle of a robotic arm therapy device"></div>
    <h1 class="headline">Grand<br>Opening</h1>
    <p class="subtitle">KESTREL MOTION THERAPY</p>
    <section class="details">
      <p class="details-label">EVENT:</p>
      <p class="details-value">Thursday, June 1st, 2023 from 12pm-6pm</p>
      <p class="details-label">LOCATION:</p>
      <p class="details-value">58240 Harlan Crest Ave, Pinegate Hollow, MI 48917</p>
    </section>
    <div class="brand">
      <span class="brand-dot"></span>
      <span class="brand-name">Kestrel Motion Therapy</span>
    </div>
  </article>
</main>
</body>
</html>
```